Swimming Pool Business Billboard

10' x 24' Billboard displaying company name, logo and phone number. Picture of swimming pool activity; kids playing , swimming, etc. Bullet points possibly shown: New Construction, Repairs, Weekly maintenance.

Industry/Entity Type

Swimming pool construction, repairs and maintenance.

Font styles to use
Sans Serif

Colors
0054AA
0677BA
7BADD7
CADEEF
E8F1F8

Requirements
Must have
• Rusty & Calder Pembrook, RUSTY'S POOLS & Service,
Nice to have
• Prefer to have my last name "Pembrook" above the word "POOLS" only in smaller print so that "RUSTYS POOLS" is distinguished.

```html
<!DOCTYPE html>
<html lang="en">
<head>
<meta charset="utf-8">
<title>Rusty's Pools &amp; Service Billboard</title>
<link rel="stylesheet" href="https://fonts.googleapis.com/css2?family=Roboto+Slab:wght@400;800&family=Roboto+Condensed:wght@700&family=Montserrat:wght@800&family=Poppins:wght@400;500;600&display=swap">
<style>
  :root {
    --navy: #1d3a6b;
    --sky: #0bc0f5;
    --white: #ffffff;
    --ink: #0d0d12;
    --water-deep: #2a8fd0;
    --water-light: #8fd0f2;
    --page: #ffffff;
  }
  * { margin: 0; padding: 0; box-sizing: border-box; }
  html, body { width: 1071px; height: 1200px; overflow: hidden; background: var(--page); }
  .billboard {
    position: absolute; left: 48px; top: 397px; width: 975px; height: 405px;
    background: var(--white); overflow: hidden;
    box-shadow: 0 6px 14px rgba(0,0,0,.25);
  }
  .photo {
    position: absolute; left: 560px; top: 0; width: 415px; height: 336px;
    background:
      radial-gradient(ellipse at 60% 30%, rgba(255,255,255,.55), transparent 55%),
      linear-gradient(180deg, var(--water-light), var(--water-deep));
  }
  .photo-fade {
    position: absolute; left: 540px; top: 0; width: 110px; height: 336px;
    background: linear-gradient(90deg, var(--white) 20%, rgba(255,255,255,0));
  }
  .brand-mark {
    position: absolute; left: 8px; top: 12px; width: 124px; height: 170px;
    display: flex; flex-direction: column; align-items: center; justify-content: center; gap: 10px;
  }
  .brand-mark .dot { width: 78px; height: 78px; border-radius: 50%; background: var(--navy); }
  .brand-mark .name {
    font-family: "Roboto Slab", serif; font-weight: 800; font-size: 17px; color: var(--navy);
  }
  .owners {
    position: absolute; left: 161px; top: 26px; width: 410px; height: 34px;
    background: var(--navy);
    clip-path: polygon(0 100%, 14px 0, 100% 0, calc(100% - 14px) 100%);
    color: var(--white); font-family: "Roboto Slab", serif; font-weight: 400;
    font-size: 27px; line-height: 34px; text-align: center;
  }
  .title {
    position: absolute; left: 138px; top: 62px; width: 462px; text-align: center;
    font-family: "Roboto Slab", serif; font-weight: 800; font-size: 54px;
    line-height: 58px; color: var(--navy); letter-spacing: -0.5px;
  }
  .subtitle {
    position: absolute; left: 138px; top: 118px; width: 462px; text-align: center;
    font-family: "Roboto Condensed", sans-serif; font-weight: 700; font-size: 56px;
    line-height: 60px; color: var(--sky);
  }
  .divider {
    position: absolute; left: 40px; top: 182px; width: 540px; height: 2px;
    background: linear-gradient(90deg, transparent, var(--sky) 30%, var(--sky) 70%, transparent);
  }
  .services {
    position: absolute; left: 24px; top: 190px; list-style: none;
    font-family: "Montserrat", sans-serif; font-weight: 800; font-size: 34px;
    line-height: 43px; color: var(--ink); letter-spacing: 0.5px;
  }
  .services li { display: flex; align-items: center; }
  .services li::before {
    content: ""; width: 12px; height: 12px; border-radius: 50%;
    background: var(--sky); margin-right: 17px;
  }
  .contact-bar {
    position: absolute; left: 0; top: 336px; width: 975px; height: 69px;
    display: flex; font-family: "Poppins", sans-serif; color: var(--white);
  }
  .contact { display: flex; align-items: center; gap: 6px; height: 100%; }
  .contact svg { flex: none; }
  .contact.phone { width: 280px; background: var(--navy); padding-left: 24px; font-weight: 600; font-size: 33px; letter-spacing: -0.5px; }
  .contact.email { width: 283px; background: var(--sky); padding-left: 12px; font-weight: 500; font-size: 21px; }
  .contact.address { flex: 1; background: var(--navy); padding-left: 12px; font-weight: 400; font-size: 17px; }
</style>
</head>
<body>
<main class="billboard">
  <div class="photo" role="img" aria-label="Photo of a smiling child swimming in a sparkling blue pool with a colourful float"></div>
  <div class="photo-fade"></div>

  <div class="brand-mark">
    <span class="dot"></span>
    <span class="name">Rusty's Pools</span>
  </div>

  <div class="owners">Rusty &amp; Calder Pembrook</div>
  <h1 class="title">RUSTY'S POOLS</h1>
  <div class="subtitle">&amp; SERVICE</div>
  <div class="divider"></div>

  <ul class="services">
    <li>NEW CONSTRUCTION</li>
    <li>REPAIRS &amp; MAINTENANCE</li>
    <li>WEEKLY MAINTENANCE</li>
  </ul>

  <footer class="contact-bar">
    <div class="contact phone">
      <svg width="20" height="20" viewBox="0 0 20 20"><circle cx="10" cy="10" r="10" fill="var(--sky)"/><path d="M7 5l2 2-1 1.5c.6 1.4 1.6 2.4 3 3L12.5 10l2 2-1.3 1.6C9.8 13.6 6.4 10.2 5.4 6.6z" fill="var(--white)"/></svg>
      912-555-0147
    </div>
    <div class="contact email">
      <svg width="20" height="20" viewBox="0 0 20 20"><circle cx="10" cy="10" r="10" fill="var(--white)"/><rect x="5" y="6.5" width="10" height="7" rx="1" fill="none" stroke="var(--sky)" stroke-width="1.4"/><path d="M5.5 7l4.5 3.5L14.5 7" fill="none" stroke="var(--sky)" stroke-width="1.4"/></svg>
      rusty@rcpools.net
    </div>
    <div class="contact address">
      <svg width="20" height="20" viewBox="0 0 20 20"><circle cx="10" cy="10" r="10" fill="var(--sky)"/><path d="M10 4.5a3.6 3.6 0 0 0-3.6 3.6c0 2.7 3.6 6.9 3.6 6.9s3.6-4.2 3.6-6.9A3.6 3.6 0 0 0 10 4.5z" fill="none" stroke="var(--white)" stroke-width="1.3"/><circle cx="10" cy="8.1" r="1.3" fill="var(--white)"/></svg>
      2750 Marlow Bend Rd Fernhill, GA 31599
    </div>
  </footer>
</main>
</body>
</html>
```